Ski and Snowboard Instructor Business card

An eye catching business card capturing the essence of the sport and the mountain with a professional finish and easily readable contact information.

Notes on uploaded files:
I must have the KORVE (Northern Guild of Alpine Coaching Standards) Logo featured on the design (I designed it on the front but you can move if you think it would look better else where). The front of the card as you will see is a picture of a mountain top, if you can find a real image of this with a clear blue sky and snow that would be great -even better if it was from New Zealand as that is where I will be using the card!!! but also I am open to creative ones - logo style, 2D mountain outline etc.
As for the back something clean and simple, I originally designed it as matt black background with stylised writing for my name and a contrasting colour for the other writing. Possibly add the tag line 'certified snowsports instructor' I didn't just because of spacing etc but I'm keen to see what you guys come up with.

Writing on the back
Jamie Whitcombe
SKI - SNOWBOARD
jamiewhitcombe2008@frostmail.example
NZ: 02107481639
UK: (+44) 07835519402
Hope this helps
Happy designing!

Industry/Entity Type

Business

Contact Information for Business Card

See description

Requirements
Must have
• KORVE (Northern guild of Alpine Coaching Standards) logo. It is a trademarked logo so please no alterations in shape or colour.
Nice to have
• Real Images of mountains, snow etc

```html
<!DOCTYPE html>
<html lang="en">
<head>
<meta charset="utf-8">
<title>Jamie Whitcombe — Ski &amp; Snowboard Instructor Business Card</title>
<link rel="stylesheet" href="https://fonts.googleapis.com/css2?family=Quicksand:wght@300;400;500;600&display=swap">
<style>
  :root {
    --page-bg: #e9e7e3;
    --card-white: #ffffff;
    --accent-blue: #2f6fe0;
    --accent-blue-deep: #1f4fb3;
    --matt-black: #0b0b0c;
    --ink-light: #f4f6f8;
    --ink-muted: #9aa1a8;
    --sky-top: #6d8fb5;
    --sky-low: #b9cbe0;
    --rock: #4c5561;
    --snow: #eef2f6;
    --brand-red: #c8262e;
  }
  * { box-sizing: border-box; margin: 0; padding: 0; }
  html, body {
    width: 1200px; height: 2324px; overflow: hidden;
    background: var(--page-bg);
    font-family: "Quicksand", "Helvetica Neue", Arial, sans-serif;
  }
  .sheet {
    position: relative; width: 1200px; height: 2324px;
    display: flex; flex-direction: column; align-items: center; justify-content: center; gap: 160px;
  }
  .card {
    position: relative; width: 1000px; height: 620px; overflow: hidden;
    border-radius: 6px;
    box-shadow: 0 10px 30px rgba(0,0,0,0.18);
  }

  /* Front */
  .card-front { background: var(--card-white); }
  .mountain-photo {
    position: absolute; inset: 0;
    background:
      linear-gradient(165deg, transparent 52%, rgba(238,242,246,0.95) 78%, var(--snow) 100%),
      linear-gradient(180deg, var(--sky-top) 0%, var(--sky-low) 28%, var(--rock) 52%, #8e99a6 64%, var(--snow) 82%);
  }
  .brand-badge {
    position: absolute; top: 36px; right: 0;
    width: 330px; height: 150px;
    background: var(--card-white);
    border-radius: 75px 0 0 75px;
    display: flex; flex-direction: column; justify-content: center;
    padding-left: 46px;
  }
  .brand-name {
    display: flex; align-items: center; gap: 14px;
    font-size: 54px; font-weight: 600; color: var(--accent-blue-deep); letter-spacing: 2px;
  }
  .brand-dot { width: 34px; height: 34px; border-radius: 50%; background: var(--brand-red); }
  .brand-full {
    margin-top: 6px; font-size: 13px; font-weight: 500; color: var(--accent-blue-deep);
    line-height: 1.25; width: 230px;
  }
  .name-band {
    position: absolute; left: 0; top: 420px;
    width: 800px; height: 92px;
    background: var(--accent-blue);
    border-radius: 0 46px 46px 0;
    display: flex; align-items: center; padding-left: 60px;
  }
  .name-band .holder-name {
    font-size: 54px; font-weight: 400; color: var(--ink-light); letter-spacing: 0.5px;
  }

  /* Back */
  .card-back { background: var(--matt-black); color: var(--ink-light); }
  .snow-splatter {
    position: absolute; inset: 0;
    background:
      radial-gradient(ellipse 180px 420px at 0% 30%, rgba(235,238,242,0.85), transparent 70%),
      radial-gradient(ellipse 320px 130px at 95% 0%, rgba(235,238,242,0.75), transparent 70%),
      radial-gradient(ellipse 260px 90px at 20% 100%, rgba(235,238,242,0.6), transparent 70%);
  }
  .back-content { position: absolute; left: 210px; top: 150px; right: 0; }
  .back-name { font-size: 66px; font-weight: 300; letter-spacing: 1px; }
  .discipline-bar {
    margin-top: 16px; height: 58px;
    background: var(--accent-blue);
    border-radius: 29px 0 0 29px;
    display: flex; align-items: center; padding-left: 28px;
    font-size: 30px; font-weight: 500; letter-spacing: 2px;
  }
  .contact-list { margin-top: 34px; list-style: none; font-size: 22px; line-height: 1.55; font-weight: 400; }
  .contact-list .label { color: var(--ink-muted); margin-right: 6px; }
  .tagline {
    position: absolute; left: 210px; bottom: 40px;
    font-size: 18px; color: var(--ink-muted); letter-spacing: 1px;
  }
</style>
</head>
<body>
<main class="sheet">
  <section class="card card-front" aria-label="Business card front">
    <div class="mountain-photo" role="img" aria-label="Photograph of a snowy mountain summit under a clear blue sky"></div>
    <div class="brand-badge">
      <div class="brand-name"><span class="brand-dot"></span>KORVE</div>
      <div class="brand-full">Northern Guild of Alpine Coaching Standards</div>
    </div>
    <div class="name-band"><span class="holder-name">Jamie Whitcombe</span></div>
  </section>

  <section class="card card-back" aria-label="Business card back">
    <div class="snow-splatter" role="img" aria-label="White snow splatter texture around the card edges"></div>
    <div class="back-content">
      <h1 class="back-name">Jamie Whitcombe</h1>
      <div class="discipline-bar">SKI • SNOWBOARD</div>
      <ul class="contact-list">
        <li>jamiewhitcombe2008@frostmail.example</li>
        <li><span class="label">NZ:</span>02107481639</li>
        <li><span class="label">UK:</span>(+44) 07835519402</li>
      </ul>
    </div>
    <p class="tagline">certified snowsports instructor</p>
  </section>
</main>
</body>
</html>
```